We are a Leadership Specialist Boutique Business that is launching a residential womans workshop....

We need a post card which will include our logo, an overview of our workshop, a catch statement on one side and on the other side dates, venue, facilitators and contacts to book the workshop. The postcards will be distributed at an Global Sisterhood Harvest Lunch. They will be placed at each setting of the lunch attendees. The company QBR running the lunch is a sponsor of our business.

Target Market(s)

Women supervisor to middle management positions or own business

Industry/Entity Type

Academic Training

Font styles to use
Serif

Colors
34a7d8

Requirements
Must have
• Use Colour Palette on docs attached, Logo, Workshop overview either the Circle Theory or the Core Philosophy Text,
• The dates, venue, all costs of the program including discount code. One catch sentence that grabs the audience from the content I have provided that appeals to the designer
• Must have these contacts.
• Website: brightpathforwardgroup.com,au
• Email: Info@brightpathforwardgroup.com.au.
• Phone: 0419372605
Nice to have
• Facilitators Photos and names

```html
<!DOCTYPE html>
<html lang="en">
<head>
<meta charset="utf-8">
<title>Bright Path Forward – Workshop Postcard</title>
<link rel="stylesheet" href="https://fonts.googleapis.com/css2?family=Raleway:wght@400;500;700;800;900&display=swap">
<style>
  :root {
    --mint: #addfd4;
    --ink: #1b1b1b;
    --charcoal: #3b3b3d;
    --paper: #ffffff;
    --backdrop: #eceded;
    --photo-tone: #9a9a9a;
  }
  * { box-sizing: border-box; margin: 0; padding: 0; }
  html, body { width: 1200px; height: 498px; overflow: hidden; }
  body {
    background: var(--backdrop);
    font-family: "Raleway", Arial, sans-serif;
    color: var(--ink);
    position: relative;
  }
  .postcard {
    position: absolute;
    top: 64px;
    width: 525px;
    height: 370px;
    background: var(--paper);
    overflow: hidden;
  }
  .postcard--front { left: 64px; }
  .postcard--back { left: 612px; }

  /* Front: brand panel */
  .brand-panel {
    position: absolute; left: 0; top: 0;
    width: 271px; height: 100%;
    background: var(--mint);
    text-align: center;
  }
  .brand-mark {
    position: absolute; left: 0; right: 0; top: 118px;
    display: flex; align-items: center; justify-content: center; gap: 10px;
  }
  .brand-mark__dot {
    width: 26px; height: 26px; border-radius: 50%;
    background: var(--ink); flex: none;
  }
  .brand-mark__name {
    font-weight: 800; font-size: 26px; line-height: 1.05;
    text-align: left; color: var(--ink);
  }
  .contact-phone {
    position: absolute; left: 0; right: 0; top: 280px;
    font-weight: 800; font-size: 31px; letter-spacing: 0.5px;
  }
  .contact-line {
    position: absolute; left: 0; right: 0;
    font-weight: 700; font-size: 11.5px;
  }
  .contact-line--web { top: 321px; }
  .contact-line--mail { top: 337px; }

  /* Front: philosophy panel */
  .philosophy {
    position: absolute; left: 271px; top: 0;
    width: 254px; height: 100%;
    text-align: center; color: var(--charcoal);
  }
  .philosophy__title {
    margin-top: 41px;
    font-weight: 800; font-size: 18px; line-height: 1.28;
    color: var(--charcoal);
  }
  .pillar { margin-top: 13px; }
  .pillar:first-of-type { margin-top: 16px; }
  .pillar__name { font-weight: 800; font-size: 13px; letter-spacing: 0.2px; }
  .pillar__text { font-size: 12px; line-height: 1.25; margin: 0 auto; }
  .pillar__text--narrow { width: 170px; }
  .catch-band {
    position: absolute; left: 0; right: 0; top: 318px; height: 34px;
    background: var(--charcoal); color: var(--paper);
    font-size: 11px; line-height: 1.3;
    display: flex; align-items: center; justify-content: center;
    text-align: center;
  }

  /* Back */
  .details-panel {
    position: absolute; left: 0; top: 0;
    width: 273px; height: 100%;
    background: var(--mint);
    text-align: center;
  }
  .facilitator {
    position: absolute; top: 30px; width: 120px;
  }
  .facilitator--one { left: 16px; }
  .facilitator--two { left: 134px; }
  .facilitator__photo {
    width: 93px; height: 93px; margin: 0 auto;
    border-radius: 50%;
    border: 1.5px solid var(--charcoal);
    background: radial-gradient(circle at 50% 40%, #d4d4d4, var(--photo-tone));
  }
  .facilitator__name { margin-top: 5px; font-weight: 700; font-size: 12px; }
  .facilitator__role { font-weight: 700; font-size: 8.5px; line-height: 1.25; }
  .program {
    position: absolute; left: 14px; top: 188px;
    width: 245px; height: 112px;
    border: 2px solid var(--ink);
    font-size: 7.5px; line-height: 1.3;
  }
  .program__title {
    position: relative; top: -8px;
    display: inline-block; padding: 0 4px;
    background: var(--mint);
    font-weight: 700; font-size: 11.5px;
  }
  .program__dates { margin-top: -6px; }
  .program__subtitle { font-weight: 700; font-size: 11px; margin-top: 2px; }
  .program__price { font-weight: 800; font-style: italic; margin-top: 5px; }
  .details-phone {
    position: absolute; left: 0; right: 0; top: 313px;
    font-weight: 800; font-size: 31px; letter-spacing: 0.5px;
  }
  .stamp-box {
    position: absolute; left: 438px; top: 30px;
    width: 62px; height: 64px;
    background: var(--charcoal);
  }
  .address-line {
    position: absolute; left: 292px; width: 208px; height: 1px;
    background: var(--charcoal);
  }
  .address-line--1 { top: 264px; }
  .address-line--2 { top: 301px; }
  .address-line--3 { top: 338px; }
</style>
</head>
<body>

<section class="postcard postcard--front">
  <div class="brand-panel">
    <div class="brand-mark">
      <span class="brand-mark__dot"></span>
      <span class="brand-mark__name">Bright Path<br>Forward</span>
    </div>
    <div class="contact-phone">0419372605</div>
    <div class="contact-line contact-line--web">brightpathforwardgroup.com,au</div>
    <div class="contact-line contact-line--mail">Info@brightpathforwardgroup.com.au</div>
  </div>

  <div class="philosophy">
    <h1 class="philosophy__title">THE CORE PHILOSOPHY<br>OF THE PROGRAMZ</h1>
    <div class="pillar">
      <h2 class="pillar__name">WORLDVIEW</h2>
      <p class="pillar__text">A view Held inside of us<br>as to how things work.</p>
    </div>
    <div class="pillar">
      <h2 class="pillar__name">BIASES</h2>
      <p class="pillar__text">Our own behaviours and the<br>behaviours of others that<br>reinforce this worldviews.</p>
    </div>
    <div class="pillar">
      <h2 class="pillar__name">ERROR SCRIPTS</h2>
      <p class="pillar__text pillar__text--narrow">Stories implanted by us or others that limits our potential.</p>
    </div>
    <p class="catch-band">Rewiting a new Personal Narrative allows<br>us to shatter our own glass celing</p>
  </div>
</section>

<section class="postcard postcard--back">
  <div class="details-panel">
    <div class="facilitator facilitator--one">
      <div class="facilitator__photo" role="img" aria-label="Black and white portrait photo of facilitator Dana Whitford"></div>
      <p class="facilitator__name">Dana Whitford</p>
      <p class="facilitator__role">An intutive advisor to<br>empowered women</p>
    </div>
    <div class="facilitator facilitator--two">
      <div class="facilitator__photo" role="img" aria-label="Black and white portrait photo of facilitator Oliver Hastings"></div>
      <p class="facilitator__name">Oliver Hastings</p>
      <p class="facilitator__role">Trusted Advisor to<br>wise women</p>
    </div>

    <div class="program">
      <h2 class="program__title">Program and Upcoming Dates</h2>
      <p class="program__dates">2 ½ Days residential – 26th to 28th May 2019<br>May Venue - The Larchmont Lodge, Riverbend NSW<br>Future Programs - August, October, March</p>
      <h3 class="program__subtitle">Why</h3>
      <p>The program is emersive and wholistic which includes<br>development of your life and leadership skills, by rewriting<br>your narrative and a personal action plan for change</p>
      <p class="program__price">$3,495 (Early Bird Book by 26th April) $3,095<br>Quote QBR Code 9455 for a further $100 Discount</p>
    </div>

    <div class="details-phone">0419372605</div>
  </div>

  <div class="stamp-box"></div>
  <span class="address-line address-line--1"></span>
  <span class="address-line address-line--2"></span>
  <span class="address-line address-line--3"></span>
</section>

</body>
</html>
```